New Company Business Card Design

I have a new company logo and I want a new business card design. I dont know if the logo file i attached is in the correct format or quality. We are a New York City Specialty construction Firm specializing in high risk out of the box projects. I want a simple and classy business card that people will his card is as crisp as the work his company does.

Target Market(s)

Clients in the heavy construction industry in New York City

Industry/Entity Type

Construction Company

Contact Information for Business Card

Simple Classy - DIFFERENT

Font styles to use
Other font styles liked:
• Mach the logo font in some way

Colors

Designer to choose colors to be used in the design.

Requirements
Must have
• Uniqueness
Nice to have
• Nothing particular - Just different and classy - Timeless
Should not have
• Goofy Shit or Gimmicky shit

```html
<!DOCTYPE html>
<html lang="en">
<head>
<meta charset="utf-8">
<title>Korvel Associates, Inc. — Business Card</title>
<link rel="stylesheet" href="https://fonts.googleapis.com/css2?family=Roboto:ital,wght@0,400;0,500;0,700;1,400&display=swap">
<style>
  :root {
    --backdrop: #3f2618;
    --card-white: #ffffff;
    --brand-blue: #0a5cb0;
    --brand-blue-light: #04a2e3;
    --brand-blue-deep: #0a4a9a;
    --skyline-blue: #0b4593;
    --text-light: #ffffff;
  }
  * { margin: 0; padding: 0; box-sizing: border-box; }
  html, body {
    width: 1200px;
    height: 1200px;
    overflow: hidden;
  }
  body {
    position: relative;
    background: var(--backdrop);
    font-family: "Roboto", Arial, sans-serif;
  }
  .card {
    position: absolute;
    box-shadow: 0 6px 18px rgba(0, 0, 0, 0.35);
  }

  /* Front */
  .card-front {
    left: 218px;
    top: 131px;
    width: 752px;
    height: 429px;
    background: var(--card-white);
    overflow: hidden;
  }
  .card-front .accent-band {
    position: absolute;
    left: 0;
    right: 0;
    bottom: 0;
    height: 11px;
    background: var(--brand-blue);
  }
  .brand-mark {
    position: absolute;
    left: 0;
    right: 0;
    top: 178px;
    display: flex;
    align-items: center;
    justify-content: center;
    gap: 16px;
  }
  .brand-mark .brand-square {
    width: 44px;
    height: 44px;
    background: var(--brand-blue);
  }
  .brand-mark .brand-name {
    font-size: 44px;
    font-weight: 700;
    color: var(--brand-blue);
    letter-spacing: 1px;
    line-height: 1;
  }

  /* Back */
  .card-back {
    left: 217px;
    top: 630px;
    width: 765px;
    height: 438px;
    background: linear-gradient(to bottom, var(--brand-blue-light) 0%, #0688d4 30%, var(--brand-blue-deep) 100%);
    overflow: hidden;
    color: var(--text-light);
  }
  .holder {
    position: absolute;
    left: 54px;
    top: 128px;
  }
  .holder .holder-name {
    font-size: 53px;
    font-weight: 500;
    line-height: 1;
    letter-spacing: -0.5px;
  }
  .holder .holder-title {
    font-size: 25px;
    font-weight: 500;
    margin-top: 2px;
    margin-left: 9px;
    line-height: 1;
  }
  .contact {
    position: absolute;
    left: 396px;
    top: 135px;
    display: grid;
    grid-template-columns: 87px auto;
    row-gap: 8px;
    font-size: 18px;
    line-height: 22px;
  }
  .contact .label {
    font-style: italic;
    font-weight: 400;
  }
  .contact .value {
    font-weight: 500;
  }
  .skyline {
    position: absolute;
    left: 0;
    right: 0;
    bottom: 0;
    height: 96px;
    background: linear-gradient(to bottom, rgba(11, 69, 147, 0.55), var(--skyline-blue));
  }
</style>
</head>
<body>
  <section class="card card-front">
    <div class="brand-mark">
      <span class="brand-square"></span>
      <span class="brand-name">Korvel Associates, Inc.</span>
    </div>
    <div class="accent-band"></div>
  </section>

  <section class="card card-back">
    <div class="holder">
      <div class="holder-name">YOUR NAME</div>
      <div class="holder-title">job title</div>
    </div>
    <div class="contact">
      <span class="label">address.</span>
      <span class="value">123 Lorem Ipsum,<br>Lorem, California 12345</span>
      <span class="label">email.</span>
      <span class="value">youremail@yourdomain.com</span>
      <span class="label">phone.</span>
      <span class="value">123.456.7891</span>
    </div>
    <div class="skyline" role="img" aria-label="Silhouette of a city skyline along the bottom edge"></div>
  </section>
</body>
</html>
```